Bright Path Therapies business cards and stationary

Need business cards and stationary designed to match previously made logo for for a new company based in Sydney NSW called 'Bright Path Therapies'.

We provide early intervention services and diagnostic assessment for children with disability and their families. I would like designs that are colourful and child friendly - possibly using feet/footprints/steps on a white background. The final design should communicate that we are family friendly, accepting and fun to work with.

Target Market(s)

Parents and Families
Teachers
Allied Health Professionals

Industry/Entity Type

Psychology

Contact Information for Business Card

Bright Path Therapies
www.brightpaththerapies.example
info@brightpaththerapies.example

Font styles to use
Sans Serif
Decorative
Script

Requirements
Must have
• Match the font and colour scheme of logo, along with footprint picture
Nice to have
• Clean and simple, while reflecting that I am working with families.
• Also- editable for when we make staff specific cards.

```html
<!DOCTYPE html>
<html lang="en">
<head>
<meta charset="utf-8">
<title>Bright Path Therapies – Business Card</title>
<link href="https://fonts.googleapis.com/css2?family=Roboto:wght@400;500&display=swap" rel="stylesheet">
<style>
  :root {
    --backdrop: #e6e6e6;
    --card: #f7f7f7;
    --brand-red: #ef4136;
    --brand-blue: #2a7bc8;
    --text: #4a4a4a;
    --shadow: rgba(0,0,0,0.18);
  }
  * { margin: 0; padding: 0; box-sizing: border-box; }
  html, body { width: 1200px; height: 960px; overflow: hidden; }
  body {
    background: var(--backdrop);
    font-family: "Roboto", Arial, sans-serif;
    color: var(--text);
    position: relative;
  }
  .card {
    position: absolute;
    left: 320px;
    width: 600px;
    background: var(--card);
    border-radius: 18px;
    box-shadow: 0 3px 8px var(--shadow);
    overflow: hidden;
  }
  .card--front { top: 100px; height: 350px; }
  .card--back { top: 493px; height: 342px; }

  .brand {
    position: absolute;
    top: 140px;
    left: 0; right: 0;
    display: flex;
    align-items: center;
    justify-content: center;
    gap: 16px;
  }
  .brand__dot {
    width: 56px; height: 56px;
    border-radius: 50%;
    background: var(--brand-red);
  }
  .brand__name {
    font-size: 36px;
    font-weight: 500;
    color: var(--brand-blue);
    letter-spacing: 0.5px;
  }
  .tagline {
    position: absolute;
    top: 282px;
    left: 0; right: 0;
    text-align: center;
    font-size: 14px;
    line-height: 19px;
  }

  .brand-shape {
    position: absolute;
    left: -110px;
    top: -110px;
    width: 420px;
    height: 420px;
    border-radius: 50%;
    background: var(--brand-red);
  }
  .contact {
    position: absolute;
    right: 32px;
    top: 121px;
    text-align: right;
  }
  .contact__name {
    font-size: 19px;
    font-weight: 500;
    color: var(--brand-red);
    line-height: 24px;
  }
  .contact__role {
    font-size: 14px;
    font-weight: 500;
    color: var(--brand-blue);
    line-height: 22px;
    margin-bottom: 10px;
  }
  .contact__address {
    font-size: 14px;
    line-height: 19px;
    margin-bottom: 11px;
    margin-right: 2px;
  }
  .contact__lines { list-style: none; }
  .contact__lines li {
    font-size: 14px;
    line-height: 19px;
    display: flex;
    justify-content: flex-end;
    align-items: center;
    gap: 7px;
  }
  .icon { width: 13px; height: 13px; fill: var(--brand-red); flex: none; }
</style>
</head>
<body>

  <section class="card card--front">
    <div class="brand">
      <span class="brand__dot"></span>
      <span class="brand__name">Bright Path Therapies</span>
    </div>
    <p class="tagline">Early intervention services &amp; diagnostic assessment<br>for children with disability and their families.</p>
  </section>

  <section class="card card--back">
    <div class="brand-shape" role="img" aria-label="Large red brand shape in the card corner"></div>
    <div class="contact">
      <p class="contact__name">MAYA LARKIN</p>
      <p class="contact__role">CEO/FOUNDER</p>
      <p class="contact__address">42 Wattle Street<br>Parramatta NSW 2150</p>
      <ul class="contact__lines">
        <li>555 203 7716
          <svg class="icon" viewBox="0 0 16 16" aria-hidden="true"><path d="M3.5 1l2.5 3-1.5 2a9 9 0 0 0 5 5l2-1.5 3 2.5-1.5 2.5C7 15 1 9 1 2.5z"/></svg>
        </li>
        <li>555 391 0482
          <svg class="icon" viewBox="0 0 16 16" aria-hidden="true"><path d="M4 0h8a1 1 0 0 1 1 1v14a1 1 0 0 1-1 1H4a1 1 0 0 1-1-1V1a1 1 0 0 1 1-1zm1 2v10h6V2zm3 11a1 1 0 1 0 0 2 1 1 0 0 0 0-2z"/></svg>
        </li>
        <li>555 647 2059
          <svg class="icon" viewBox="0 0 16 16" aria-hidden="true"><path d="M4 1h8v4H4zM1 6h14v6h-3v3H4v-3H1zm4 4v3h6v-3z"/></svg>
        </li>
        <li>info@brightpaththerapies.example
          <svg class="icon" viewBox="0 0 16 16" aria-hidden="true"><path d="M1 3h14v1L8 9 1 4zm0 2.5l7 5 7-5V13H1z"/></svg>
        </li>
        <li>www.brightpaththerapies.example
          <svg class="icon" viewBox="0 0 16 16" aria-hidden="true"><circle cx="8" cy="8" r="7"/><path d="M1 8h14M8 1c-3 3-3 11 0 14M8 1c3 3 3 11 0 14" stroke="#f7f7f7" stroke-width="1.2" fill="none"/></svg>
        </li>
      </ul>
    </div>
  </section>

</body>
</html>
```